Square Business Cards for Our Restaurant / Event Venue

We need square business cards designed for the management team of our event venue and restaurant. On one side of the card should be the the Harbor Lantern 7 logo and URL www.harborlantern7.example. On the other side should be the Ember Logo and URL www.emberhall7.example. All employee details should be on the side with Ember logo. There will be a total of 5 cards to be created with the design.

Clara Bennquist
clara@harborlantern7.example

main 555.418.3072
direct 555.730.2946

4831 West Orchard Lane SE
Washington, DC 90417

Industry/Entity Type

Business

```html
<!DOCTYPE html>
<html lang="en">
<head>
<meta charset="utf-8">
<title>Ember / Harbor Lantern 7 — Square Business Cards</title>
<link rel="stylesheet" href="https://fonts.googleapis.com/css2?family=Lato:wght@300;400;700&display=swap">
<style>
  :root {
    --backdrop: #dfe4e6;
    --card-light: #f2f2f1;
    --card-dark: #2b2727;
    --ink: #1c1c1c;
    --ink-soft: #3a3a3a;
    --accent-red: #b3232a;
    --muted-light: #b9b4b2;
  }
  * { box-sizing: border-box; margin: 0; padding: 0; }
  html, body { width: 1200px; height: 682px; overflow: hidden; }
  body {
    background: var(--backdrop);
    font-family: "Lato", sans-serif;
    display: flex;
    align-items: center;
    justify-content: center;
    gap: 60px;
  }
  .card {
    width: 430px;
    height: 430px;
    box-shadow: 0 6px 18px rgba(0,0,0,0.14);
    display: flex;
    flex-direction: column;
    align-items: center;
    justify-content: center;
    text-align: center;
  }
  .card--front { background: var(--card-light); color: var(--ink-soft); }
  .card--back { background: var(--card-dark); color: var(--muted-light); }

  .brand-mark {
    display: flex;
    align-items: center;
    gap: 10px;
    font-weight: 700;
    font-size: 46px;
    color: var(--ink);
    margin-bottom: 26px;
  }
  .brand-mark__dot {
    width: 12px; height: 12px; border-radius: 50%;
    background: var(--accent-red);
  }
  .staff-name {
    font-weight: 400;
    font-size: 25px;
    letter-spacing: 1px;
    text-transform: uppercase;
    color: var(--ink);
    line-height: 1.1;
  }
  .staff-name__last { color: var(--accent-red); }
  .staff-email { font-size: 14px; font-weight: 300; margin-bottom: 16px; }
  .phone-list { font-size: 16px; line-height: 1.25; margin-bottom: 16px; }
  .phone-list__label { color: var(--accent-red); font-weight: 400; margin-right: 4px; }
  .address { font-size: 16px; font-weight: 300; line-height: 1.25; margin-bottom: 16px; }
  .site-url { font-size: 15px; font-weight: 300; letter-spacing: 0.5px; }

  .venue-mark {
    display: flex;
    align-items: center;
    gap: 16px;
    margin-bottom: 40px;
  }
  .venue-mark__circle {
    width: 60px; height: 60px; border-radius: 50%;
    background: var(--accent-red);
  }
  .venue-mark__name {
    font-weight: 300;
    font-size: 30px;
    color: var(--muted-light);
  }
  .card--back .site-url { font-size: 14px; letter-spacing: 2px; }
</style>
</head>
<body>
  <section class="card card--front" aria-label="Front of business card">
    <div class="brand-mark">
      <span class="brand-mark__name">Ember</span>
      <span class="brand-mark__dot" aria-hidden="true"></span>
    </div>
    <p class="staff-name">Clara <span class="staff-name__last">Bennquist</span></p>
    <p class="staff-email">clara@harborlantern7.example</p>
    <p class="phone-list">
      <span class="phone-list__label">main</span>555.418.3072<br>
      <span class="phone-list__label">direct</span>555.730.2946
    </p>
    <p class="address">4831 West Orchard Lane SE<br>Washington, DC 90417</p>
    <p class="site-url">www.emberhall7.example</p>
  </section>

  <section class="card card--back" aria-label="Back of business card">
    <div class="venue-mark">
      <span class="venue-mark__circle" aria-hidden="true"></span>
      <span class="venue-mark__name">Harbor Lantern 7</span>
    </div>
    <p class="site-url">www.harborlantern7.example</p>
  </section>
</body>
</html>
```